Book Cover Design

Design with title STEADFAST
Subtitle: How Kindle the Spark of Resolve
Author Name: Corin Lea Mabbott
Put DAILY HARBOR POST BESTSELLER at top
Shimmer design, see inspirational images attached

```html
<!DOCTYPE html>
<html lang="en">
<head>
<meta charset="utf-8">
<title>STEADFAST — Corin Lea Mabbott</title>
<link href="https://fonts.googleapis.com/css2?family=Questrial&display=swap" rel="stylesheet">
<style>
  :root {
    --ink: #ffffff;
    --shadow: rgba(40, 44, 52, 0.75);
    --cream: #eef0e4;
    --sand: #cfc4b2;
    --mist: #e6efec;
    --teal: #a9cbd6;
    --sea: #b3dcd8;
    --sky: #b4d4e6;
    --lavender: #b6b9dc;
    --violet: #a09cc4;
    --pale: #d6dcea;
  }
  html, body {
    margin: 0;
    padding: 0;
    width: 800px;
    height: 1200px;
    overflow: hidden;
  }
  .cover {
    position: relative;
    width: 800px;
    height: 1200px;
    overflow: hidden;
    font-family: "Questrial", "Century Gothic", sans-serif;
    color: var(--ink);
    background:
      radial-gradient(ellipse 420px 260px at 110px 40px, rgba(245, 246, 234, 0.9), transparent 70%),
      radial-gradient(ellipse 380px 300px at 740px 60px, rgba(200, 188, 168, 0.9), transparent 70%),
      radial-gradient(ellipse 360px 220px at 330px 300px, rgba(234, 242, 238, 0.95), transparent 70%),
      radial-gradient(ellipse 300px 180px at 560px 420px, rgba(240, 240, 234, 0.85), transparent 70%),
      radial-gradient(ellipse 500px 160px at 420px 620px, rgba(160, 198, 210, 0.7), transparent 70%),
      radial-gradient(ellipse 300px 160px at 760px 740px, rgba(176, 222, 214, 0.8), transparent 70%),
      radial-gradient(ellipse 260px 220px at 40px 800px, rgba(170, 212, 228, 0.85), transparent 70%),
      radial-gradient(ellipse 360px 200px at 360px 900px, rgba(206, 224, 236, 0.9), transparent 70%),
      radial-gradient(ellipse 420px 260px at 120px 1160px, rgba(156, 152, 196, 0.95), transparent 70%),
      radial-gradient(ellipse 360px 240px at 700px 1120px, rgba(206, 212, 236, 0.9), transparent 70%),
      linear-gradient(160deg, var(--cream) 0%, var(--sand) 14%, var(--mist) 28%, var(--teal) 48%, var(--sky) 66%, var(--lavender) 84%, var(--violet) 100%);
  }
  .cover__text {
    position: absolute;
    left: 0;
    width: 800px;
    text-align: center;
    white-space: nowrap;
    text-transform: uppercase;
    line-height: 1;
    text-shadow: 2px 2px 2px var(--shadow);
  }
  .bestseller-tag {
    top: 36px;
    font-size: 20px;
    letter-spacing: 7px;
    padding-left: 7px;
    text-shadow: 1px 1px 1px var(--shadow);
  }
  .author-name {
    top: 79px;
    font-size: 48px;
    letter-spacing: 16px;
    padding-left: 16px;
  }
  .book-title {
    top: 466px;
    font-size: 120px;
    letter-spacing: 3px;
    padding-left: 3px;
    text-shadow: 3px 3px 3px var(--shadow);
  }
  .book-subtitle {
    top: 1062px;
    font-size: 43px;
    letter-spacing: 13px;
    padding-left: 13px;
    line-height: 51px;
  }
</style>
</head>
<body>
  <main class="cover">
    <p class="cover__text bestseller-tag" style="margin:0">Daily Harbor Post Bestseller</p>
    <p class="cover__text author-name" style="margin:0">Corin Lea Mabbott</p>
    <h1 class="cover__text book-title" style="margin:0;font-weight:400">Steadfast</h1>
    <h2 class="cover__text book-subtitle" style="margin:0;font-weight:400">How Kindle<br>the Spark of Resolve</h2>
  </main>
</body>
</html>
```